Need a simple buisness card for my plumbing business. Would like it to be black background with white text.

Industry/Entity Type

Business

Requirements
Must have
• On the front of the card I need to have,
TKW PLUMBING SERVICES
PLUMBERS, DRAINERS & GASFITTERS
Dorian Lessop
0491576038
Info@tkwplumbingservices.com.au
LIC No 518047k
ABN No 57091836254
On the back I need in point form
Domestic,industrial,commercial, all new installations, renovations, sewer renewals, repairs,
Fully licensed and insured
Nice to have
• A nice simple logo

```html
<!DOCTYPE html>
<html lang="en">
<head>
<meta charset="utf-8">
<title>TKW Plumbing Services – Business Card</title>
<link rel="stylesheet" href="https://fonts.googleapis.com/css2?family=Open+Sans:ital,wght@0,700;1,400;1,600;1,700&family=Didact+Gothic&display=swap">
<style>
  :root {
    --page: #ffffff;
    --card-black: #000000;
    --text-white: #ffffff;
    --text-soft: #e6e6e6;
    --bubble-fill: #ffffff;
    --bubble-text: #1a1a1a;
    --back-glow: #4a4a4a;
    --back-mid: #1e1e1e;
    --back-edge: #0a0a0a;
    --shadow: rgba(0,0,0,0.35);
  }
  * { margin: 0; padding: 0; box-sizing: border-box; }
  html, body {
    width: 1117px; height: 1200px; overflow: hidden;
    background: var(--page);
  }
  .canvas { position: relative; width: 1117px; height: 1200px; }
  .card {
    position: absolute; left: 154px; width: 820px; height: 451px;
    background: var(--card-black); color: var(--text-white);
    box-shadow: 3px 4px 6px var(--shadow);
    overflow: hidden;
  }
  .card--front { top: 98px; }
  .card--back { top: 627px; }
  .abs { position: absolute; line-height: 1; white-space: nowrap; }

  .company-name {
    left: 27px; top: 30px;
    font: 700 32px "Open Sans", sans-serif; letter-spacing: 0.3px;
  }
  .company-trades {
    left: 27px; top: 70px;
    font: italic 400 22px "Didact Gothic", sans-serif; letter-spacing: 1.2px;
  }
  .contact-name {
    left: 421px; top: 214px;
    font: italic 400 28px "Didact Gothic", sans-serif; letter-spacing: 0.5px;
  }
  .contact-list, .licence-list {
    position: absolute; list-style: none;
    font: italic 600 17px "Open Sans", sans-serif; line-height: 24.5px;
  }
  .contact-list { left: 421px; top: 365px; }
  .licence-list { left: 27px; top: 387px; }
  .contact-list span { display: inline-block; width: 28px; }

  .brand-mark {
    position: absolute; display: flex; align-items: center; gap: 6px;
    font: 700 20px "Open Sans", sans-serif; color: var(--text-white);
  }
  .brand-mark .dot {
    width: 12px; height: 12px; border-radius: 50%; background: var(--text-white);
  }
  .card--front .brand-mark { left: 726px; top: 42px; }
  .card--back .brand-mark { left: 726px; top: 338px; }

  .back-texture {
    position: absolute; inset: 0;
    background: radial-gradient(ellipse 55% 70% at 40% 40%, var(--back-glow) 0%, var(--back-mid) 55%, var(--back-edge) 100%);
  }
  .services-bubble { position: absolute; left: 256px; top: 37px; }
  .services-bubble__label {
    position: absolute; left: 0; top: 0; width: 310px; height: 50px;
    display: flex; align-items: center; justify-content: center;
    font: italic 700 21px "Open Sans", sans-serif; color: var(--bubble-text);
    letter-spacing: 0.6px;
  }
  .services-list {
    position: absolute; left: 268px; top: 142px; list-style: none;
    font: italic 400 27px "Didact Gothic", sans-serif; color: var(--text-soft);
    line-height: 33px; letter-spacing: 0.6px;
  }
  .services-list li::before {
    content: "•"; display: inline-block; width: 21px; font-size: 20px;
    vertical-align: top; line-height: 33px;
  }
  .assurance {
    left: 151px; top: 408px;
    font: italic 400 30px "Didact Gothic", sans-serif; color: var(--text-soft);
    letter-spacing: 2px;
  }
</style>
</head>
<body>
<main class="canvas">
  <section class="card card--front" aria-label="Business card front">
    <h1 class="abs company-name">TKW PLUMBING SERVICES</h1>
    <p class="abs company-trades">PLUMBERS, DRAINERS &amp; GASFITTERS</p>
    <div class="brand-mark"><span class="dot"></span>TKW</div>
    <p class="abs contact-name">Dorian Lessop</p>
    <ul class="licence-list">
      <li>LIC No 518047k</li>
      <li>ABN No 57091836254</li>
    </ul>
    <ul class="contact-list">
      <li><span>T:</span>0491576038</li>
      <li><span>E:</span>Info@tkwplumbingservices.com.au</li>
      <li><span>W:</span>www.tkwplumbingservices.com.au</li>
    </ul>
  </section>

  <section class="card card--back" aria-label="Business card back">
    <div class="back-texture" role="img" aria-label="Dark metallic mesh texture background"></div>
    <div class="services-bubble">
      <svg width="310" height="66" viewBox="0 0 310 66" aria-hidden="true">
        <path d="M22 1.5 H288 A20.5 20.5 0 0 1 308.5 22 V28 A20.5 20.5 0 0 1 288 48.5 H166 L156 62 L146 48.5 H22 A20.5 20.5 0 0 1 1.5 28 V22 A20.5 20.5 0 0 1 22 1.5 Z"
              fill="var(--bubble-fill)" stroke="var(--back-edge)" stroke-width="3"/>
      </svg>
      <p class="services-bubble__label">Our Services included</p>
    </div>
    <ul class="services-list">
      <li>Domestic</li>
      <li>industrial</li>
      <li>commercial</li>
      <li>all new installations</li>
      <li>renovations</li>
      <li>sewer renewals</li>
      <li>repairs</li>
    </ul>
    <div class="brand-mark"><span class="dot"></span>TKW</div>
    <p class="abs assurance">Fully licensed and insured</p>
  </section>
</main>
</body>
</html>
```